Bold Truck Branding needed for plumbing company

We have a new logo that needs to be adapted for vehicle branding. The new logo and photos of the truck are attached to the brief. We would like the logo to be oversized so it stands out.
We are a plumbing company that specializes in bathroom renovations but we also do service work and maintenance. The script that should be included is detailed in the must haves.

Requirements
Must have
• Logo and company name should be on the back along with the phone number. The website will not be listed on the truck. The following script should be written as bullet points. - Complete bathroom renovations - Water heaters and toilet installs - All residential plumbing
Nice to have
• Oversized logo. Should go over the canopy and can be slightly cut off by the wheel if necessary.

```html
<!DOCTYPE html>
<html lang="en">
<head>
<meta charset="utf-8">
<title>Harlow Plumbing – Vehicle Wrap</title>
<link rel="stylesheet" href="https://fonts.googleapis.com/css2?family=Montserrat:wght@500;600;700;800&display=swap">
<style>
  :root {
    --page: #ffffff;
    --wrap-blue: #3d9de0;
    --wrap-charcoal: #2f3238;
    --wrap-black: #1f2125;
    --ink-white: #ffffff;
  }
  * { margin: 0; padding: 0; box-sizing: border-box; }
  html, body {
    width: 1200px;
    height: 1200px;
    overflow: hidden;
    background: var(--page);
  }
  .wrap-layout {
    display: block;
    width: 1200px;
    height: 1200px;
    font-family: "Montserrat", sans-serif;
  }
  .panel-blue { fill: var(--wrap-blue); }
  .panel-charcoal { fill: var(--wrap-charcoal); }
  .panel-black { fill: var(--wrap-black); }
  .brand-ring { fill: none; stroke: var(--ink-white); }
  .brand-name { fill: var(--ink-white); font-weight: 700; }
  .brand-descriptor { fill: var(--ink-white); font-weight: 700; letter-spacing: 0.32em; }
  .bullet-dot { fill: var(--wrap-blue); }
  .bullet-item { fill: var(--ink-white); font-weight: 600; }
  .phone-number { fill: var(--ink-white); font-weight: 800; }
  .service-list { fill: var(--ink-white); font-weight: 500; white-space: pre; }
</style>
</head>
<body>
<svg class="wrap-layout" viewBox="0 0 1200 1200" xmlns="http://www.w3.org/2000/svg">

  <g class="side-wrap">
    <rect class="panel-blue" x="0" y="141" width="1200" height="455"/>
    <polygon class="panel-charcoal"
      points="200,165 1200,165 1200,596 1010,596 880,488 430,430 200,430"/>
    <circle class="brand-ring" cx="211" cy="273" r="102" stroke-width="14"/>
    <text class="brand-name" x="330" y="372" font-size="118">HARLOW</text>
    <text class="brand-descriptor" x="440" y="432" font-size="46">PLUMBING</text>
  </g>

  <g class="rear-wrap">
    <rect class="panel-blue" x="290" y="680" width="650" height="445" rx="18"/>
    <polygon class="panel-charcoal" points="365,712 850,712 892,848 328,848"/>
    <rect class="panel-black" x="382" y="848" width="468" height="90"/>
    <rect class="panel-black" x="352" y="952" width="530" height="148" rx="6"/>

    <circle class="brand-ring" cx="455" cy="780" r="44" stroke-width="7"/>
    <text class="brand-name" x="512" y="792" font-size="52">HARLOW</text>
    <text class="brand-descriptor" x="556" y="826" font-size="22">PLUMBING</text>

    <g class="service-bullets">
      <circle class="bullet-dot" cx="446" cy="867" r="5"/>
      <text class="bullet-item" x="460" y="873" font-size="18">Complete bathroom renovations</text>
      <circle class="bullet-dot" cx="446" cy="892" r="5"/>
      <text class="bullet-item" x="460" y="898" font-size="18">Water heaters and toilet installs</text>
      <circle class="bullet-dot" cx="446" cy="917" r="5"/>
      <text class="bullet-item" x="460" y="923" font-size="18">All residential plumbing</text>
    </g>

    <text class="phone-number" x="617" y="1036" font-size="68" text-anchor="middle">555-014-2368</text>
    <text class="service-list" x="617" y="1080" font-size="18" text-anchor="middle">Bathroom Renovation   I   Service   I   Maintenance</text>
  </g>

</svg>
</body>
</html>
```